Brightvantage.com tech company website

Current site is www.brightvantage.com. The site will tell you about our company.

Designs we like are:
http://megainfo.quellorix.com
www.trelvo.com
www.morvasket.com

Target Market(s)

B2B

Industry/Entity Type

It Company

Coding

Coded - Design and coding required

Number of Pages Required

5+ page

Requirements
Must have
• We want to entice without giving away too much info. We like graphics and colors. But website must look official and credible.

```html
<!DOCTYPE html>
<html lang="en">
<head>
<meta charset="utf-8">
<title>Brightvantage — Big Data</title>
<link rel="stylesheet" href="https://fonts.googleapis.com/css2?family=Montserrat:wght@400;600;700;800&family=Open+Sans:wght@400;600&display=swap">
<style>
:root{
  --navy:#1d4a78;
  --navy-deep:#173d63;
  --sky:#5cb8ea;
  --sky-light:#8fd0f2;
  --accent:#3a9ad9;
  --ink:#2b3a4a;
  --muted:#7b8794;
  --line:#dde3ea;
  --paper:#ffffff;
  --mist:#f2f4f6;
  --map:#e6e8eb;
}
*{margin:0;padding:0;box-sizing:border-box}
html,body{width:1200px;height:2472px;overflow:hidden}
body{font-family:"Open Sans",Arial,sans-serif;color:var(--ink);background:var(--paper)}
h1,h2,h3,.brand,.nav a,.btn,.case-num{font-family:"Montserrat",Arial,sans-serif}

.topbar{height:64px;display:flex;align-items:center;justify-content:space-between;padding:0 90px}
.brand{display:flex;align-items:center;gap:10px;font-weight:800;font-size:24px;color:var(--navy);letter-spacing:.5px}
.brand-dot{width:26px;height:26px;border-radius:50%;background:var(--sky)}
.contact-line{display:flex;gap:26px;font-size:13px;color:var(--muted)}
.contact-line span b{color:var(--accent);font-weight:600;margin-right:6px}

.nav{height:36px;background:var(--navy);display:flex;align-items:center;padding:0 90px;gap:0}
.nav a{color:#fff;text-decoration:none;font-size:12px;font-weight:600;text-transform:uppercase;letter-spacing:.6px;padding:0 22px;line-height:36px}
.nav a.active{background:var(--accent)}

.hero{height:340px;background:var(--sky);position:relative;display:flex;align-items:center;padding:0 90px}
.hero-copy{width:430px;color:#fff}
.hero h1{font-size:42px;font-weight:800;line-height:1.08;text-transform:uppercase;letter-spacing:.5px}
.hero p{font-size:15px;margin:16px 0 24px;line-height:1.5;color:#eaf6fd}
.btn{display:inline-block;font-size:11px;font-weight:700;letter-spacing:1px;text-transform:uppercase;padding:10px 22px;border-radius:2px}
.btn-outline{border:2px solid #fff;color:#fff}
.btn-solid{background:var(--accent);color:#fff}
.hero-art{position:absolute;right:90px;top:40px;width:560px;height:260px;border-radius:6px;background:linear-gradient(135deg,var(--sky-light),#4aa6dd)}

.services{height:590px;background:var(--mist);padding:60px 90px 0;text-align:center}
.section-title{font-size:26px;font-weight:700;color:var(--navy);text-transform:uppercase;letter-spacing:.5px}
.section-title.light{color:#fff}
.section-intro{max-width:820px;margin:14px auto 0;font-size:13px;line-height:1.6;color:var(--muted)}
.service-grid{display:flex;justify-content:center;gap:34px;margin-top:48px}
.service-card{width:240px;background:var(--paper);border:1px solid var(--line);padding:28px 22px 26px;text-align:center}
.service-card svg{display:block;margin:0 auto 16px}
.service-card h3{font-size:12px;font-weight:700;color:var(--accent);text-transform:uppercase;letter-spacing:.5px;line-height:1.4}
.service-card p{font-size:12px;line-height:1.6;color:var(--muted);margin:10px 0 20px;min-height:96px}

.cases{height:390px;background:#ecedef;padding:54px 90px 0;text-align:center;position:relative}
.case-grid{display:flex;justify-content:center;gap:40px;margin-top:36px}
.case-item{width:250px;height:190px;padding:24px 20px;text-align:left}
.case-item.featured{background:var(--sky);color:#fff}
.case-num{font-size:56px;font-weight:800;color:var(--accent);line-height:1}
.case-item.featured .case-num{color:#fff}
.case-item p{font-size:12px;font-weight:600;text-transform:uppercase;line-height:1.5;margin-top:14px;color:var(--accent)}
.case-item.featured p{color:#fff}
.case-arrow{position:absolute;top:230px}
.case-arrow.left{left:150px}
.case-arrow.right{right:150px}

.why{height:480px;background:var(--navy);padding:54px 90px 0;position:relative}
.why .section-title{text-align:center}
.why-intro{text-align:center;color:#c6d6e6;font-size:13px;margin:14px auto 0;max-width:720px;line-height:1.6}
.why-list{list-style:none;margin-top:40px;width:480px}
.why-list li{color:#e3ecf5;font-size:13px;line-height:1;padding:9px 0 9px 26px;position:relative}
.why-list li svg{position:absolute;left:0;top:7px}
.why-art{position:absolute;right:90px;top:150px;width:500px;height:280px;border-radius:6px;background:linear-gradient(135deg,#2d6aa3,#1a4470)}

.location{height:350px;position:relative;background:var(--map)}
.map-area{position:absolute;inset:0;background:linear-gradient(180deg,#eceef0,#dfe2e6)}
.map-pin{position:absolute;left:470px;top:110px}
.contact-card{position:absolute;left:540px;top:90px;width:260px;background:var(--paper);padding:22px 24px;box-shadow:0 2px 10px rgba(0,0,0,.12);font-size:12px;line-height:1.8;color:var(--muted)}
.contact-card h3{font-size:13px;color:var(--navy);font-weight:700;margin-bottom:6px;text-transform:uppercase}

.footer-nav{height:50px;background:var(--navy-deep);display:flex;align-items:center;justify-content:space-between;padding:0 90px}
.footer-nav nav{display:flex;gap:24px}
.footer-nav nav a{color:#fff;text-decoration:none;font-size:11px;font-weight:600;font-family:"Montserrat",Arial,sans-serif}
.socials{display:flex;gap:8px}
.socials span{width:20px;height:20px;border-radius:50%;background:#fff;display:block}
.footer-base{height:172px;display:flex;flex-direction:column;align-items:center;justify-content:center;gap:10px}
.footer-base .brand{font-size:20px}
.footer-base small{font-size:11px;color:var(--muted)}
</style>
</head>
<body>

<header class="topbar">
  <div class="brand"><span class="brand-dot"></span>Brightvantage</div>
  <div class="contact-line">
    <span><b>Email:</b>info@brightvantage.com</span>
    <span><b>Call:</b>(555) 014-2290</span>
  </div>
</header>

<nav class="nav">
  <a href="#" class="active">Home</a>
  <a href="#">About Us</a>
  <a href="#">Big Data Analytics</a>
  <a href="#">Perception and Influence</a>
  <a href="#">Case Studies</a>
  <a href="#">Contact Us</a>
</nav>

<section class="hero">
  <div class="hero-copy">
    <h1>Biggest, Best &amp; Boldest Uses of Big Data</h1>
    <p>Big data solutions, customer-focused insights, and smart analytics designed to grow your business.</p>
    <span class="btn btn-outline">Learn More</span>
  </div>
  <div class="hero-art" role="img" aria-label="Illustration of big data concepts: charts, cloud storage and connected devices around the words Big Data"></div>
</section>

<section class="services">
  <h2 class="section-title">Services Offered by Our Big Data Division</h2>
  <p class="section-intro">Brightvantage's data division helps companies collect, analyze and act on information at scale. From targeted campaigns to secure data storage, our team delivers measurable results that move your business forward every quarter.</p>
  <div class="service-grid">
    <article class="service-card">
      <svg width="60" height="60" viewBox="0 0 60 60" fill="none" stroke="#3a9ad9" stroke-width="2"><circle cx="30" cy="30" r="24"/><circle cx="30" cy="30" r="15"/><circle cx="30" cy="30" r="6"/></svg>
      <h3>Truly Targeted Marketing</h3>
      <p>Reach the right buyers with campaigns shaped by real behavior data, so every message lands where it matters most.</p>
      <span class="btn btn-solid">Learn More</span>
    </article>
    <article class="service-card">
      <svg width="60" height="60" viewBox="0 0 60 60" fill="none" stroke="#3a9ad9" stroke-width="2"><path d="M8 12h44L34 32v16l-8 4V32z"/></svg>
      <h3>Lead Generation</h3>
      <p>Fill your pipeline with qualified prospects found through predictive scoring and careful analysis of market signals.</p>
      <span class="btn btn-solid">Learn More</span>
    </article>
    <article class="service-card">
      <svg width="60" height="60" viewBox="0 0 60 60" fill="none" stroke="#3a9ad9" stroke-width="2"><ellipse cx="30" cy="14" rx="18" ry="6"/><path d="M12 14v32c0 3.3 8 6 18 6s18-2.7 18-6V14M12 30c0 3.3 8 6 18 6s18-2.7 18-6"/></svg>
      <h3>Data Management</h3>
      <p>Store, clean and organize your information securely, with tools that keep records accurate and ready for use.</p>
      <span class="btn btn-solid">Learn More</span>
    </article>
  </div>
</section>

<section class="cases">
  <h2 class="section-title">Case Studies</h2>
  <p class="section-intro">The following are recent case studies from our clients. For more information, contact us.</p>
  <svg class="case-arrow left" width="16" height="24" viewBox="0 0 16 24"><path d="M13 2L3 12l10 10" fill="none" stroke="#3a9ad9" stroke-width="3"/></svg>
  <div class="case-grid">
    <div class="case-item featured">
      <div class="case-num">01.</div>
      <p>Identified new sales for a Fortune 500 client using our core system</p>
    </div>
    <div class="case-item">
      <div class="case-num">02.</div>
      <p>Initial public offering management for financial services co.</p>
    </div>
    <div class="case-item">
      <div class="case-num">03.</div>
      <p>Increased sales with our truly targeted marketing service</p>
    </div>
  </div>
  <svg class="case-arrow right" width="16" height="24" viewBox="0 0 16 24"><path d="M3 2l10 10L3 22" fill="none" stroke="#3a9ad9" stroke-width="3"/></svg>
</section>

<section class="why">
  <h2 class="section-title light">Why Choose Us?</h2>
  <p class="why-intro">We combine deep industry knowledge with modern analytics to give every client clear answers, faster decisions and lasting value.</p>
  <ul class="why-list">
    <li><svg width="14" height="14" viewBox="0 0 14 14"><path d="M2 7l3 3 7-7" fill="none" stroke="#5cb8ea" stroke-width="2"/></svg>Proven track record across dozens of industries</li>
    <li><svg width="14" height="14" viewBox="0 0 14 14"><path d="M2 7l3 3 7-7" fill="none" stroke="#5cb8ea" stroke-width="2"/></svg>Dedicated analysts assigned to every single account</li>
    <li><svg width="14" height="14" viewBox="0 0 14 14"><path d="M2 7l3 3 7-7" fill="none" stroke="#5cb8ea" stroke-width="2"/></svg>Secure infrastructure built on modern cloud platforms</li>
    <li><svg width="14" height="14" viewBox="0 0 14 14"><path d="M2 7l3 3 7-7" fill="none" stroke="#5cb8ea" stroke-width="2"/></svg>Transparent reporting with clear monthly performance reviews</li>
    <li><svg width="14" height="14" viewBox="0 0 14 14"><path d="M2 7l3 3 7-7" fill="none" stroke="#5cb8ea" stroke-width="2"/></svg>Flexible pricing that scales with your growth</li>
    <li><svg width="14" height="14" viewBox="0 0 14 14"><path d="M2 7l3 3 7-7" fill="none" stroke="#5cb8ea" stroke-width="2"/></svg>Fast onboarding with minimal disruption to teams</li>
    <li><svg width="14" height="14" viewBox="0 0 14 14"><path d="M2 7l3 3 7-7" fill="none" stroke="#5cb8ea" stroke-width="2"/></svg>Custom dashboards tailored to your key goals</li>
    <li><svg width="14" height="14" viewBox="0 0 14 14"><path d="M2 7l3 3 7-7" fill="none" stroke="#5cb8ea" stroke-width="2"/></svg>Responsive support from real people, every day</li>
  </ul>
  <div class="why-art" role="img" aria-label="Illustration of a desktop monitor, laptop, tablet and phone showing analytics dashboards"></div>
</section>

<section class="location">
  <div class="map-area" role="img" aria-label="Street map showing the office location"></div>
  <svg class="map-pin" width="36" height="48" viewBox="0 0 36 48"><path d="M18 2C9 2 2 9 2 18c0 12 16 28 16 28s16-16 16-28C34 9 27 2 18 2z" fill="#3a9ad9"/><circle cx="18" cy="18" r="6" fill="#fff"/></svg>
  <div class="contact-card">
    <h3>Contact Us</h3>
    1200 Harbor Lane, Suite 300<br>
    Lakeview, MN 55401<br>
    (555) 014-2290<br>
    info@brightvantage.com
  </div>
</section>

<footer>
  <div class="footer-nav">
    <nav>
      <a href="#">Home</a>
      <a href="#">About Us</a>
      <a href="#">Big Data Analytics</a>
      <a href="#">Perception and Influence</a>
      <a href="#">Case Studies</a>
      <a href="#">Contact Us</a>
    </nav>
    <div class="socials"><span></span><span></span><span></span></div>
  </div>
  <div class="footer-base">
    <div class="brand"><span class="brand-dot"></span>Brightvantage</div>
    <small>Copyright © 2024 Brightvantage. All Rights Reserved.</small>
  </div>
</footer>

</body>
</html>
```